Tallowgate Tailwind Shuttle Co needs a website

We need a logo and website built for our little business. We transport Stand Up Paddle Boarders and Ocean Ski Paddlers from Byron Bay along the coast to places like Ocean Shores, Lennox Head, Ballina where they get out of the bus, hit the ocean and paddle back with the wind to Byron Bay. The website would need a link to a book now button, with a page that allows for the Byron Bay weather,wind forecast on it. Also a side bar that links to our Socialia page. We would like a weekly schedule of bus times on the website as well,

For themes I really like a ocean based hawaii styled theme if possible. Something that portrays the lifestyle and enjoyment people can have in the ocean. Perhaps a banner image that scrolls where we could also add photos as well over time of the business
Updates

Hi Designers have made the payment non refundable so someone will definitely be getting paid

cheers

Industry/Entity Type

Business

Colors
86acd3
3377b5
35a7d7
0392ce
ffffff
faee3f

Requirements
Nice to have
• Good Imagery of Byron Bay and coastline, I will provide some
A nice logo for the site
Link to a bus timetable where the client can book now, ( i use Quolvo bookings software so can get it to link to the site

```html
<!DOCTYPE html>
<html lang="en">
<head>
<meta charset="utf-8">
<title>Tallowgate Tailwind Shuttle Co</title>
<link rel="stylesheet" href="https://fonts.googleapis.com/css2?family=Open+Sans:wght@400;600;700&display=swap">
<style>
:root{
  --navy:#0f3a66;
  --blue:#1b87c9;
  --link:#1a6fc0;
  --social:#1f3f8a;
  --text:#333;
  --muted:#6a6a6a;
  --white:#fff;
  --orange-top:#ff8a1e;
  --orange-bottom:#f05a0a;
  --sand:#d8b98d;
}
*{box-sizing:border-box;margin:0;padding:0}
html,body{width:1183px;height:1200px;overflow:hidden}
body{font-family:"Open Sans",sans-serif;color:var(--text);background:var(--sand)}
.stage{position:relative;width:1200px;height:1217px;transform:scale(0.9858);transform-origin:0 0;
  background:linear-gradient(180deg,#1577cc 0%,#3d9ee2 16%,#7cc0ee 26%,#3d98d8 36%,#1f7fc4 42%,#4aa6d6 46%,#e8f3f5 49%,#e6d3b3 51%,var(--sand) 56%,var(--sand) 100%)}
.abs{position:absolute}
.social-btn{left:888px;top:40px;width:181px;height:27px;background:var(--social);border-radius:3px;color:var(--white);font-size:12.5px;font-weight:600;display:flex;align-items:center;gap:10px;padding-left:8px}
.social-btn .sq{width:16px;height:16px;background:var(--white);opacity:.85;border-radius:2px}
.header{left:131px;top:78px;width:939px;height:74px;background:var(--white)}
.brand{position:absolute;left:17px;top:14px;font-size:36px;font-weight:700;color:var(--navy);display:flex;align-items:center;gap:8px}
.brand .dot{width:14px;height:14px;border-radius:50%;background:var(--blue)}
.nav{position:absolute;left:326px;top:29px;display:flex;gap:28px;font-size:15.5px;font-weight:600;color:var(--text)}
.nav .active{color:var(--blue)}
.book-btn{position:absolute;left:804px;top:18px;width:114px;height:40px;border-radius:3px;background:linear-gradient(var(--orange-top),var(--orange-bottom));color:var(--white);font-weight:700;font-size:16px;display:flex;align-items:center;justify-content:center}
.slider{left:131px;top:161px;width:938px;height:422px;background:radial-gradient(ellipse at 24% 18%,#fff3b0 0%,#f2b65a 12%,#8a7a6a 32%,#2f3a44 60%,#1d2730 100%)}
.arrow{position:absolute;top:174px;width:60px;height:60px;border-radius:50%;background:rgba(255,255,255,.8)}
.arrow.prev{left:21px}.arrow.next{left:866px}
.arrow svg{width:60px;height:60px}
.sec-title{font-size:15px;font-weight:700;color:var(--navy);letter-spacing:.2px}
.panel{background:var(--white)}
.welcome{left:130px;top:643px;width:380px;height:455px}
.welcome .photo{position:absolute;left:11px;top:10px;width:356px;height:258px;background:linear-gradient(180deg,#8fb0cc 0%,#5a86b0 35%,#2a6aa8 55%,#1d5f9e 100%)}
.welcome p{position:absolute;left:11px;top:288px;width:356px;font-size:10.4px;line-height:24px;color:var(--muted);text-align:justify}
.schedule{left:530px;top:643px;width:539px;height:283px}
table{border-collapse:collapse;width:100%;font-size:11px;text-align:center}
th{color:var(--blue);font-weight:700;height:47px;line-height:18px;font-size:11px}
td{height:39.4px;border-top:1px solid #f0f0f0}
td a{color:var(--link)}
.cb{display:inline-block;width:12px;height:12px;border:1px solid #999;background:#f6f6f6;vertical-align:middle}
.weather{left:531px;top:976px;width:262px;height:121px;font-size:11px;color:#666}
.weather .temp{position:absolute;left:45px;top:52px;font-size:30px;color:#222}
.weather .sun{position:absolute;left:13px;top:58px;width:24px;height:24px;border-radius:50%;background:#fde06a}
.weather .stats{position:absolute;left:136px;top:56px;font-size:7.5px;line-height:11px;color:#888}
.weather .tabs{position:absolute;left:136px;top:95px;display:flex;border:1px solid #ccc;font-size:6px;color:#555}
.weather .tabs span{padding:2px 6px;background:#eee;border-right:1px solid #ccc}
.contact{left:808px;top:976px;width:262px;height:121px;padding:13px 15px;font-size:12.5px;color:#666;line-height:24px}
.contact .fb{color:var(--navy);font-weight:700}
.contact .url{font-size:10px;line-height:18px}
.footer-nav{left:130px;top:1140px;font-size:12.5px;color:#555;display:flex;gap:16px}
.copy{left:132px;top:1175px;font-size:12.5px;color:#555}
.partner{left:940px;top:1150px;display:flex;align-items:center;gap:10px;color:var(--white);font-size:30px;font-weight:700}
.partner .dot{width:30px;height:30px;border-radius:50%;background:var(--white)}
</style>
</head>
<body>
<div class="stage">
  <div class="abs social-btn"><span class="sq"></span>Connect with Socialia</div>

  <header class="abs header">
    <div class="brand"><span>SwellRun</span><span class="dot"></span></div>
    <nav class="nav"><span class="active">HOME</span><span>ABOUT US</span><span>SERVICES</span><span>FAQ’S</span><span>CONTACT US</span></nav>
    <div class="book-btn">BOOK NOW</div>
  </header>

  <div class="abs slider" role="img" aria-label="Sunset over the bay seen from the bow of an ocean ski, a yacht on the horizon">
    <div class="arrow prev"><svg viewBox="0 0 60 60"><path d="M35 18 L23 30 L35 42" fill="none" stroke="#555" stroke-width="6" stroke-linecap="round"/></svg></div>
    <div class="arrow next"><svg viewBox="0 0 60 60"><path d="M25 18 L37 30 L25 42" fill="none" stroke="#555" stroke-width="6" stroke-linecap="round"/></svg></div>
  </div>

  <h2 class="abs sec-title" style="left:131px;top:607px">WELCOME TO BUS BOOKING SERVICE</h2>
  <h2 class="abs sec-title" style="left:530px;top:607px">BUS SCHEDULES</h2>

  <section class="abs panel welcome">
    <div class="photo" role="img" aria-label="Paddler on an ocean ski off a green headland"></div>
    <p>Lorem Ipsum is simply dummy text of the printing and typesetting industry. Lorem Ipsum has been the industry's standard dummy text ever since the 1500s, when an unknown printer took a galley of type and scrambled it to make a type specimen book. It has survived not only five centuries, but also the leap into electronic typesetting . Lorem Ipsum is simply dummy text of the printing and typesetting industry.</p>
  </section>

  <section class="abs panel schedule">
    <table>
      <tr><th style="width:44px"></th><th>BOOK NOW</th><th>DATE</th><th>DEP. TIME</th><th>LOAD<br>UP AT</th><th>START</th><th>FINISH</th><th>DISTANCE</th></tr>
      <tr><td><svg width="13" height="13" viewBox="0 0 13 13"><rect x=".5" y=".5" width="12" height="12" fill="#f6f6f6" stroke="#777"/><path d="M3 6.5 L5.5 9 L10 3" fill="none" stroke="#1f3f8a" stroke-width="1.6"/></svg></td><td><a>Book Now</a></td><td>1-2-2013</td><td>14.00</td><td>13.55</td><td>Byron Bay</td><td>Ocean shore</td><td>150 KM</td></tr>
      <tr><td><span class="cb"></span></td><td><a>Book Now</a></td><td>1-2-2013</td><td>14.00</td><td>13.55</td><td>Byron Bay</td><td>Ocean shore</td><td>150 KM</td></tr>
      <tr><td><span class="cb"></span></td><td><a>Book Now</a></td><td>1-2-2013</td><td>14.00</td><td>13.55</td><td>Byron Bay</td><td>Lennox</td><td>150 KM</td></tr>
      <tr><td><span class="cb"></span></td><td><a>Book Now</a></td><td>1-2-2013</td><td>14.00</td><td>13.55</td><td>Byron Bay</td><td>Ocean shore</td><td>150 KM</td></tr>
      <tr><td><span class="cb"></span></td><td><a>Book Now</a></td><td>1-2-2013</td><td>14.00</td><td>13.55</td><td>Byron Bay</td><td>Head</td><td>150 KM</td></tr>
      <tr><td><span class="cb"></span></td><td><a>Book Now</a></td><td>1-2-2013</td><td>14.00</td><td>13.55</td><td>Byron Bay</td><td>Ballina</td><td>150 KM</td></tr>
    </table>
  </section>

  <h2 class="abs sec-title" style="left:530px;top:943px">BYRON BAY WEATHER</h2>
  <h2 class="abs sec-title" style="left:806px;top:943px">CONTACT DETAILS</h2>

  <section class="abs panel weather">
    <div style="position:absolute;left:9px;top:12px">Byron Bay NSW, Australia</div>
    <div style="position:absolute;left:9px;top:27px;font-size:7.5px;line-height:10px">Thursday 4:00 pm<br>Clear</div>
    <span class="sun"></span>
    <div class="temp">26<sup style="font-size:7px;color:#888"> °C | °F</sup></div>
    <div class="stats">Precipitation: 30%<br>Humidity: 75%<br>Wind: 11 km/h</div>
    <div class="tabs"><span>Temperature</span><span>Precipitation</span><span style="border:0">Wind</span></div>
  </section>

  <section class="abs panel contact">
    <div style="font-weight:600">PH; 0400 555 018</div>
    <div>info@swellrunpaddle.example</div>
    <div class="fb">Socialia</div>
    <div class="url">https://www.socialia.example/pages/Tallowgate-Tailwind-Shuttle</div>
  </section>

  <nav class="abs footer-nav"><span>Home</span><span>|</span><span>About Us</span><span>|</span><span>Services</span><span>|</span><span>FAQ’s</span><span>|</span><span>Contact Us</span></nav>
  <div class="abs copy">Copyright ©2013 Company Name &nbsp;&nbsp;- All rights reserved</div>

  <div class="abs partner"><span class="dot"></span><span>Quolvo</span></div>
</div>
</body>
</html>
```